New Office Poster Designs

Attached you will find 3 poster designs that we found online along with our logos. Please use our logos to reference any type of color or design.
These posters will be hung around our Loan Offices.

INSTRUCTIONS: Please mimic all 3 posters (MINUS THE SMALL WRITING ON THEM THAT IS NOT IN ENGLISH IGNORE THAT)
but use our logos and colors. Also, if you can make them in Spanish as well as English that is a plus. We will also need 1 additional poster with the below wording.

Additional Poster:
Stuck in a Title Loan? Let us pay it off up to $10,000

Target Market(s)

People looking to get a loan and need money

Industry/Entity Type

Loan Industry - Consumer Lending - Fast easy loans

Requirements
Nice to have
• English and Spanish

```html
<!DOCTYPE html>
<html lang="en">
<head>
<meta charset="UTF-8">
<title>Title Loan Payoff Poster</title>
<link href="https://fonts.googleapis.com/css2?family=Inter:wght@600;700&display=swap" rel="stylesheet">
<style>
  :root {
    --backdrop: #e9e9e9;
    --poster-green: #1e5a32;
    --poster-green-dark: #174a28;
    --poster-green-light: #2b6b3e;
    --text-white: #ffffff;
    --brand-green: #1d5a33;
    --brand-red: #c4161c;
  }
  * { margin: 0; padding: 0; box-sizing: border-box; }
  html, body {
    width: 1200px;
    height: 1200px;
    overflow: hidden;
    background: var(--backdrop);
    font-family: "Inter", Arial, sans-serif;
  }
  .poster {
    position: absolute;
    left: 205px;
    top: 90px;
    width: 789px;
    height: 1019px;
    overflow: hidden;
    background: var(--poster-green);
  }
  .poster-backdrop {
    position: absolute;
    inset: 0;
    background:
      radial-gradient(ellipse at 45% 45%, var(--poster-green-light) 0%, transparent 60%),
      linear-gradient(160deg, var(--poster-green) 0%, var(--poster-green-dark) 100%);
  }
  .line {
    position: absolute;
    left: 86px;
    color: var(--text-white);
    font-weight: 700;
    line-height: 1;
    white-space: nowrap;
  }
  .headline { font-size: 65px; font-weight: 600; }
  .headline-top { top: 121px; }
  .headline-bottom { top: 201px; }
  .divider {
    position: absolute;
    left: 86px;
    top: 316px;
    width: 136px;
    height: 30px;
    background: var(--text-white);
  }
  .offer-lead { top: 397px; font-size: 35px; }
  .offer-upto { top: 454px; font-size: 52px; }
  .offer-amount { top: 524px; font-size: 96px; }
  .brand-card {
    position: absolute;
    left: 367px;
    top: 710px;
    width: 422px;
    height: 210px;
    background: var(--text-white);
    border-radius: 10px 0 0 10px;
    display: flex;
    flex-direction: column;
    align-items: center;
    justify-content: center;
    gap: 10px;
  }
  .brand-name {
    color: var(--brand-green);
    font-size: 44px;
    font-weight: 700;
    line-height: 1;
  }
  .brand-url {
    color: var(--brand-red);
    font-size: 20px;
    font-weight: 600;
    line-height: 1;
  }
</style>
</head>
<body>
  <main class="poster">
    <div class="poster-backdrop" role="img" aria-label="Scattered hundred-dollar bills tinted deep green"></div>
    <h1>
      <span class="line headline headline-top">Stuck in a</span>
      <span class="line headline headline-bottom">TITLE LOAN?</span>
    </h1>
    <div class="divider"></div>
    <p class="line offer-lead">Let us pay it off</p>
    <p class="line offer-upto">up to</p>
    <p class="line offer-amount">$10,000</p>
    <div class="brand-card">
      <span class="brand-name">Fairway Credit</span>
      <span class="brand-url">www.fairwaycredit.com</span>
    </div>
  </main>
</body>
</html>
```